Business card-Tales From The Harbor Gate

Looking for a business card. I have a website I designed "TalesFromTheHarborGate.com I am not a graphic artist and may at some point need help with my website too. Used the font "Hello Stockholm" on my website. I am a writer, looking to get published. Liked the "feel" of the cover below. No cliche typwriters, keyboards, pens. - Edgar P. Lindqvist
Updates

Not 100% sold on needing the owls, just a place to begin. I probably sounds like I'm going to be a pain to work with, I was a video production manager for 15+ years. When I would give an editor or graphic artist a project and let them run with it, the results were typically beyond my expectations. I give the idea then as the artists touch it, and adds value I could never bring to the project. Make something you would be proud of, don't try to second-guess me.

Target Market(s)

Agents, publishers, people I want to buy my book once I get it published

Industry/Entity Type

Publishing

Contact Information for Business Card

Edgar P. Lindqvist
TalesFromTheHarborGate.com
Phone #-TBD
Edgar@TalesFromTheHarbroGate.com
Maybe address; 418 N. 7th St Cheyenne, WY 82947

Colors
fcca95
3277b5

Requirements
Must have
• I like the "chromatic" feel of the attached cover. As you can see from my website, I'm an owl fan. Those pictures I took and do own the rights too. Not sure if they are approritae for a business card.
Should not have
• Cliche I like the "chromatic" feel of the attached book cover.
• I will need help with my website at some point too. I want the website to be easy for me to update, and reflect the same feel as the card. I write adventure, mystery. I have romance in my books too...Adventure of Romance, Romance of adventure, I am not sure but those words were like by an author firned of mine. They are rather "light" reading too.

```html
<!DOCTYPE html>
<html lang="en">
<head>
<meta charset="utf-8">
<title>Tales From The Harbor Gate – Business Card</title>
<link rel="stylesheet" href="https://fonts.googleapis.com/css2?family=Caveat+Brush&display=swap">
<style>
  :root {
    --peach: #fcca95;
    --blue: #3277b5;
    --card-black: #050505;
    --card-sheen: #1c1c1c;
    --backdrop: #d9d6d1;
    --photo-dark: #4a4238;
    --photo-mid: #8a7a62;
    --photo-light: #ece6da;
  }
  * { box-sizing: border-box; margin: 0; padding: 0; }
  html, body {
    width: 1200px; height: 1200px; overflow: hidden;
    background: var(--backdrop);
    font-family: "Caveat Brush", cursive;
  }
  .sheet {
    width: 1200px; height: 1200px;
    display: flex; flex-direction: column; align-items: center; justify-content: center;
    gap: 56px;
  }
  .card {
    position: relative;
    width: 900px; height: 514px;
    background: linear-gradient(120deg, var(--card-black) 0%, var(--card-sheen) 45%, var(--card-black) 70%);
    box-shadow: 0 10px 30px rgba(0,0,0,0.3);
    color: var(--peach);
    text-transform: uppercase;
    overflow: hidden;
    white-space: nowrap;
  }
  .card__frame {
    position: absolute; inset: 26px;
    border: 3px solid var(--peach);
  }
  .owl-photo {
    position: absolute;
    border-radius: 50%;
    border: 6px solid var(--blue);
    background: radial-gradient(circle at 55% 45%, var(--photo-mid) 0%, var(--photo-dark) 55%, var(--photo-light) 100%);
  }
  /* front */
  .card--front .owl-photo { left: 150px; top: 200px; width: 232px; height: 232px; }
  .front-title {
    position: absolute; left: 410px; top: 160px;
    font-size: 54px; line-height: 1.1; letter-spacing: 4px; font-weight: 400;
  }
  .front-title .line-one { color: var(--blue); display: block; padding-left: 20px; }
  .front-title .line-two { color: var(--peach); display: block; }
  /* back */
  .card--back .owl-photo { left: 110px; top: 100px; width: 190px; height: 190px; }
  .back-title {
    position: absolute; left: 60px; top: 310px;
    font-size: 40px; line-height: 1.1; letter-spacing: 3px; font-weight: 400;
  }
  .back-title .line-one { color: var(--peach); display: block; padding-left: 30px; }
  .back-title .line-two { color: var(--blue); display: block; }
  .divider { position: absolute; left: 0; top: 0; }
  .contact {
    position: absolute; left: 420px; top: 60px;
  }
  .contact__name { font-size: 44px; letter-spacing: 2px; line-height: 1; }
  .contact__role { font-size: 18px; color: var(--blue); margin: 6px 0 22px 28px; }
  .contact__list { list-style: none; font-size: 21px; letter-spacing: 1px; }
  .contact__list li { display: flex; align-items: center; gap: 12px; margin-bottom: 8px; text-transform: none; }
  .contact__list .caps { text-transform: uppercase; }
  .contact__list svg { width: 20px; height: 20px; flex: none; }
  .address {
    position: absolute; left: 420px; top: 400px;
    font-size: 24px; letter-spacing: 1px;
  }
</style>
</head>
<body>
<main class="sheet">
  <section class="card card--front">
    <div class="card__frame"></div>
    <div class="owl-photo" role="img" aria-label="Photograph of a great horned owl"></div>
    <h1 class="front-title">
      <span class="line-one">Tales From</span>
      <span class="line-two">The Harbor Gate</span>
    </h1>
  </section>

  <section class="card card--back">
    <div class="owl-photo" role="img" aria-label="Photograph of a great horned owl"></div>
    <h2 class="back-title">
      <span class="line-one">Tales From</span>
      <span class="line-two">The Harbor Gate</span>
    </h2>
    <svg class="divider" width="900" height="514" aria-hidden="true">
      <line x1="345" y1="50" x2="395" y2="320" stroke="var(--peach)" stroke-width="2"/>
    </svg>
    <div class="contact">
      <div class="contact__name">Edgar P. Lindqvist</div>
      <div class="contact__role">Writer</div>
      <ul class="contact__list">
        <li>
          <svg viewBox="0 0 24 24" aria-hidden="true"><path d="M6 3l3 4-2 2a12 12 0 0 0 8 8l2-2 4 3-2 3C10 21 3 14 3 5z" fill="none" stroke="var(--blue)" stroke-width="2"/></svg>
          <span>1234567890</span>
        </li>
        <li>
          <svg viewBox="0 0 24 24" aria-hidden="true"><g fill="none" stroke="var(--blue)" stroke-width="2"><circle cx="12" cy="12" r="9"/><ellipse cx="12" cy="12" rx="4" ry="9"/><line x1="3" y1="12" x2="21" y2="12"/></g></svg>
          <span class="caps">TalesFromTheHarborGate.com</span>
        </li>
        <li>
          <svg viewBox="0 0 24 24" aria-hidden="true"><rect x="3" y="6" width="18" height="12" fill="var(--blue)"/><path d="M3 6l9 7 9-7" fill="none" stroke="var(--card-black)" stroke-width="1.5"/></svg>
          <span class="caps">Edgar@TalesFromTheHarbroGate.com</span>
        </li>
      </ul>
    </div>
    <p class="address">418 N. 7th St Cheyenne, WY 82947</p>
  </section>
</main>
</body>
</html>
```